Business Card Design

Attached is my current Business card I do not like it but I must save the logo portion of it. Don't like the color or the lettering am looking for more architectural look in grays or taupe with the green more of a charturese color and the blue a charcoal color on a textured paper that looks more like something high-end that would appeal to an architect or a designer. We make concrete decorative items such as concrete fireplaces, sinks, tops and more.

Target Market(s)

Architects designers of Commercial and Residential - artistic features

Industry/Entity Type

Architect

Contact Information for Business Card

Maren T. Oakes President and Marketing Director
602-418-5563
email maren@velmorstoneworks.example
Showroom "Tavlin Design Center" 4126 W Harlow Row Scottsdale AZ
Fax: 602-871-2046

Font styles to use
Sans Serif

Requirements
Must have
• Architectural
Natural and earthy colors with a touch of color in the existing attached

```html
<!DOCTYPE html>
<html lang="en">
<head>
<meta charset="utf-8">
<title>Velmor Stoneworks – Business Card</title>
<link rel="stylesheet" href="https://fonts.googleapis.com/css2?family=Signika:wght@300;400&family=Arimo:wght@400&display=swap">
<style>
  :root {
    --backdrop: #6c7575;
    --paper: #f1f1f0;
    --charcoal: #5d6566;
    --chartreuse: #9cc43a;
    --ink: #4f5758;
  }
  * { margin: 0; padding: 0; box-sizing: border-box; }
  html, body {
    width: 1200px;
    height: 1042px;
    overflow: hidden;
    background: var(--backdrop);
  }
  .canvas {
    position: relative;
    width: 1200px;
    height: 1042px;
  }
  .card {
    position: absolute;
    width: 740px;
    height: 430px;
    background: var(--paper);
    box-shadow: 0 6px 18px rgba(0, 0, 0, 0.25);
  }
  .card--front { left: 90px; top: 50px; }
  .card--back  { left: 370px; top: 530px; }

  .brand {
    position: absolute;
    left: 0;
    right: 0;
    top: 0;
    bottom: 0;
    display: flex;
    align-items: center;
    justify-content: center;
    gap: 18px;
  }
  .brand__square {
    width: 34px;
    height: 34px;
    background: var(--chartreuse);
  }
  .brand__name {
    font-family: "Signika", sans-serif;
    font-weight: 400;
    font-size: 54px;
    letter-spacing: 0.5px;
    color: var(--charcoal);
  }

  .holder {
    position: absolute;
    right: 400px;
    top: 140px;
    text-align: right;
    font-family: "Signika", sans-serif;
    color: var(--charcoal);
  }
  .holder__name {
    font-weight: 300;
    font-size: 28px;
    letter-spacing: 1px;
    margin-bottom: 4px;
  }
  .holder__title {
    font-weight: 300;
    font-size: 18px;
    line-height: 22px;
    letter-spacing: 0.5px;
  }
  .divider {
    position: absolute;
    left: 358px;
    top: 120px;
    width: 2px;
    height: 175px;
    background: var(--charcoal);
  }
  .contact {
    position: absolute;
    left: 385px;
    top: 148px;
    font-family: "Arimo", sans-serif;
    font-size: 15px;
    line-height: 20px;
    color: var(--ink);
    list-style: none;
  }
</style>
</head>
<body>
<main class="canvas">
  <section class="card card--front" aria-label="Business card front">
    <div class="brand">
      <span class="brand__square" aria-hidden="true"></span>
      <span class="brand__name">Velmor Stoneworks</span>
    </div>
  </section>

  <section class="card card--back" aria-label="Business card back">
    <div class="holder">
      <p class="holder__name">Maren T. Oakes</p>
      <p class="holder__title">President and<br>Marketing Director</p>
    </div>
    <span class="divider" aria-hidden="true"></span>
    <ul class="contact">
      <li>Call 602-418-5563&nbsp;&nbsp;Fax 602-871-2046</li>
      <li>maren@velmorstoneworks.example</li>
      <li>Showroom “Tavlin Design Center”</li>
      <li>4126 W Harlow Row, Scottsdale, AZ</li>
    </ul>
  </section>
</main>
</body>
</html>
```